Bright Lantern Golf Club is a golf community dedicated to building productive relationships beginning with the unifying foundation of the great game.
Membership in the Bright Lantern Golf Club is simple, ask to join. The Membership Committee accepts a prospective member request upon confirmation of support for the club’s purpose.
The Bright Lantern Golf Club has only two rules:
1.) Create productive relationships building around an initial common thread
2.) When tempted to cut the last relationship thread, remember rule #1
Bright Lantern Golf Club members receive invitations to occasional club events but are also encouraged to create smaller events hosted by individual members. Members are not required to brand gatherings as official Bright Lantern Golf Club events. We believe when two or more of our members are together, the world gets better.
What are the dues? Members pay dues by sharing great stories, laughing often, encouraging each other to live well and by contributing to a meaningful cause outside of golf. If interested, please make a request for membership on the clubs Chatterbox page or send an email request to our Caddie Master at fairwayhost@pinemaillo.com.
If you join through our Chatterbox page, we encourage you to tag our page with testimonies about your common thread inspired experiences. For example, pictures of golf buddy trips and meaningful moments enjoying the great game with your family and friends.
We focus on what brings people together…
Target Market(s)
golfers who get the need to give back
Colors
Designer to choose colors to be used in the design.
Requirements
Must have
- clear messaging about the simple purpose vof the virtual club
- we can make up head quarter locations. like 19th holes around the world, global fairways, etc
- we do need a link to the club fairwayhost@pinemaillo.com
- logo very visible
Nice to have
- course pictures.... I can upload or send a few good ones
Should not have
- Pictures of virtual golf. I changed the summary

```html
<!DOCTYPE html>
<html lang="en">
<head>
<meta charset="utf-8">
<title>Bright Lantern Golf Club – Cover</title>
<link href="https://fonts.googleapis.com/css2?family=Libre+Baskerville:wght@400&family=Roboto:wght@400;700&family=Roboto+Condensed:wght@700&display=swap" rel="stylesheet">
<style>
  :root{
    --page:#f2f3f5;
    --ink:#1f1f1f;
    --white:#ffffff;
    --panel:#161616;
    --green:#5cbf3c;
    --green-text:#63c63d;
  }
  html,body{margin:0;padding:0;width:1200px;height:1200px;overflow:hidden;background:var(--page);}
  .cover{position:absolute;left:0;top:378px;width:1200px;height:444px;overflow:hidden;box-shadow:0 2px 6px rgba(0,0,0,.25);}
  .cover-art{position:absolute;inset:0;}
  .brand{position:absolute;left:57px;top:30px;width:140px;text-align:center;}
  .brand-dot{width:64px;height:64px;border-radius:50%;border:3px solid var(--ink);margin:0 auto 10px;box-sizing:border-box;}
  .brand-name{font-family:"Libre Baskerville",serif;font-size:16px;line-height:21px;color:var(--ink);}
  .headline{position:absolute;left:225px;top:62px;margin:0;font-weight:400;font-family:"Libre Baskerville",serif;color:var(--ink);}
  .headline-lead{font-size:29px;line-height:34px;display:block;}
  .headline-main{font-size:40px;line-height:52px;display:block;}
  .mission{position:absolute;left:130px;top:282px;width:480px;margin:0;text-align:center;font-family:"Libre Baskerville",serif;font-size:18px;line-height:30px;color:var(--white);text-shadow:0 1px 3px rgba(0,0,0,.6);white-space:nowrap;}
  .rules-title{position:absolute;left:783px;top:38px;width:376px;height:72px;border-radius:36px;background:var(--green);display:flex;flex-direction:column;justify-content:center;align-items:center;font-family:"Roboto Condensed",sans-serif;font-weight:700;font-size:23px;line-height:28px;color:var(--white);}
  .rule{position:absolute;left:756px;width:420px;display:flex;align-items:center;}
  .rule-num{flex:0 0 34px;height:34px;border-radius:50%;background:var(--green);color:var(--white);font-family:"Roboto",sans-serif;font-size:23px;display:flex;align-items:center;justify-content:center;border:2px solid var(--panel);box-shadow:0 0 0 1px var(--green);}
  .rule-text{flex:1;text-align:center;font-family:"Roboto",sans-serif;font-size:20px;line-height:25px;color:var(--white);}
  .rule-one{top:130px;}
  .rule-two{top:222px;}
  .join-note{position:absolute;left:770px;top:300px;width:400px;margin:0;text-align:center;font-family:"Roboto Condensed",sans-serif;font-weight:700;font-size:19px;line-height:25px;color:var(--green-text);}
  .contact-email{position:absolute;left:770px;top:388px;width:400px;text-align:center;font-family:"Roboto",sans-serif;font-weight:700;font-size:20px;letter-spacing:1.5px;color:var(--white);}
</style>
</head>
<body>
<section class="cover">
  <svg class="cover-art" width="1200" height="444" viewBox="0 0 1200 444">
    <defs>
      <linearGradient id="course-sky" x1="0" y1="0" x2="0" y2="1">
        <stop offset="0" stop-color="#eef2f3"/>
        <stop offset="0.45" stop-color="#dfe6e3"/>
        <stop offset="0.7" stop-color="#6f9a52"/>
        <stop offset="1" stop-color="#0e150d"/>
      </linearGradient>
      <linearGradient id="course-light" x1="0" y1="0" x2="1" y2="0">
        <stop offset="0" stop-color="#20281c" stop-opacity=".55"/>
        <stop offset="0.35" stop-color="#ffffff" stop-opacity="0"/>
        <stop offset="1" stop-color="#2a4a1f" stop-opacity=".35"/>
      </linearGradient>
      <linearGradient id="panel-tone" x1="0" y1="0" x2="0" y2="1">
        <stop offset="0" stop-color="#111111"/>
        <stop offset="0.5" stop-color="#2b2b2b"/>
        <stop offset="1" stop-color="#121212"/>
      </linearGradient>
    </defs>
    <g role="img" aria-label="Photo of golfers swinging on a sunlit green course">
      <rect width="1200" height="444" fill="url(#course-sky)"/>
      <rect width="1200" height="444" fill="url(#course-light)"/>
    </g>
    <path d="M766 0 Q640 222 770 444 L1200 444 L1200 0 Z" fill="var(--white)"/>
    <path d="M790 0 Q668 222 790 444 L1200 444 L1200 0 Z" fill="url(#panel-tone)" role="img" aria-label="Dark photo of a coastal golf course"/>
  </svg>

  <div class="brand">
    <div class="brand-dot"></div>
    <div class="brand-name">Bright Lantern<br>Golf Club</div>
  </div>

  <h1 class="headline">
    <span class="headline-lead">WE FOCUS ON WHAT BRINGS</span>
    <span class="headline-main">PEOPLE TOGETHER...</span>
  </h1>

  <p class="mission">Bright Lantern Golf Club is a virtual golf club<br>community dedicated to building productive<br>relationships beginning with the unifying<br>foundation of the great game.</p>

  <div class="rules-title"><span>THE BRIGHT LANTERN GOLF CLUB</span><span>HAS ONLY TWO RULES</span></div>

  <div class="rule rule-one"><span class="rule-num">1</span><span class="rule-text">Create productive relationships<br>building around an initial common<br>thread.</span></div>
  <div class="rule rule-two"><span class="rule-num">2</span><span class="rule-text">When tempted to cut the last rela-<br>tionship thread, remember rule #1</span></div>

  <p class="join-note">for membership on the clubs<br>Chatterbox page or send an email request to<br>our Caddie Master at</p>
  <div class="contact-email">fairwayhost@pinemaillo.com</div>
</section>
</body>
</html>
```